Business Card Design

We need a business card design for a new company based in Allen, Texas. (outside of Dallas,Texas) We offer Business Management Solutions to Entrepreneurs, as well as Corporate Businesses. Our product line offers solutions to Image, Branding, Social Media marketing, business development strategies, banking / funding solutions, just to name a few. We would like to see designs that convey strength and confidence. I have attached a sample design of our company name. Designers you may use company name as either: Vorlix or Vorlix Corporation, depending on the design layout.

Please show alternate color of Black as well.

Industry/Entity Type

Business

Contact Information for Business Card

Vorlix Corporation

2847 E. Hollowbrook Drive, STE 410
Marrowdale, TX 75981
Office: 469.318.7742
Fax: 469.318.7743

Dr. Miles Dunworth
Business Development Director

```html
<!DOCTYPE html>
<html lang="en">
<head>
<meta charset="utf-8">
<title>Vorlix Corporation Business Card</title>
<link href="https://fonts.googleapis.com/css2?family=Questrial&display=swap" rel="stylesheet">
<style>
  :root {
    --page: #e6e4e1;
    --ink-black: #1c1c1c;
    --ink-black-soft: #2a2a2a;
    --paper: #ffffff;
    --text-dark: #1e1e1e;
    --text-mid: #3a3a3a;
    --map-tone: #3c3c3c;
  }
  * { margin: 0; padding: 0; box-sizing: border-box; }
  html, body {
    width: 1200px; height: 900px; overflow: hidden;
    background: var(--page);
    font-family: "Questrial", "Helvetica Neue", Arial, sans-serif;
  }
  .sheet {
    width: 1200px; height: 900px;
    display: flex; flex-direction: column; align-items: center; justify-content: center;
    gap: 40px;
  }
  .card {
    position: relative;
    width: 700px; height: 400px;
    box-shadow: 0 6px 18px rgba(0,0,0,0.18);
    overflow: hidden;
  }

  /* Front */
  .card-front { background: var(--paper); }
  .front-band { position: absolute; inset: 0; width: 100%; height: 100%; }
  .front-wordmark {
    position: absolute; left: 34px; top: 40px;
    color: var(--paper); font-size: 78px; line-height: 1;
    letter-spacing: 1px;
  }
  .front-info {
    position: absolute; left: 340px; top: 54px; right: 34px;
    color: var(--text-dark);
  }
  .person-name { font-size: 21px; letter-spacing: 0.5px; text-transform: uppercase; color: var(--text-mid); }
  .person-title { font-size: 10.5px; letter-spacing: 0.6px; text-transform: uppercase; color: var(--text-mid); margin-top: 2px; }
  .company-name {
    font-size: 27px; font-weight: 400; letter-spacing: 1px; text-transform: uppercase;
    margin-top: 34px; padding-bottom: 8px;
    border-bottom: 2px solid var(--text-dark);
  }
  .contact-list { list-style: none; margin-top: 16px; }
  .contact-list li {
    display: flex; align-items: center; gap: 10px;
    font-size: 13px; color: var(--text-dark); line-height: 24px;
    white-space: nowrap;
  }
  .contact-list svg { width: 13px; height: 13px; fill: var(--text-dark); flex: none; }

  /* Back */
  .card-back {
    background: linear-gradient(160deg, var(--ink-black-soft), var(--ink-black));
  }
  .back-map {
    position: absolute; left: 230px; top: 28px; width: 420px; height: 200px;
    border-radius: 40px;
    background: radial-gradient(ellipse at center, var(--map-tone) 0%, rgba(60,60,60,0.4) 55%, rgba(60,60,60,0) 75%);
  }
  .back-wordmark {
    position: absolute; right: 54px; bottom: 70px;
    color: var(--paper); font-size: 96px; line-height: 1; letter-spacing: 2px;
  }
</style>
</head>
<body>
<main class="sheet">

  <section class="card card-front" aria-label="Business card front">
    <svg class="front-band" viewBox="0 0 700 400" preserveAspectRatio="none" aria-hidden="true">
      <defs>
        <linearGradient id="band-tone" x1="0" y1="0" x2="1" y2="1">
          <stop offset="0" stop-color="#2b2b2b"/>
          <stop offset="1" stop-color="#161616"/>
        </linearGradient>
      </defs>
      <polygon points="0,0 312,0 312,26 298,40 298,400 0,400" fill="url(#band-tone)"/>
    </svg>
    <div class="front-wordmark">vorlix</div>

    <div class="front-info">
      <p class="person-name">Dr. Miles Dunworth</p>
      <p class="person-title">Business Development Director</p>
      <h1 class="company-name">Vorlix Corporation</h1>
      <ul class="contact-list">
        <li>
          <svg viewBox="0 0 16 16" aria-label="Phone"><path d="M3 1h3l1.5 4-2 1.3a9 9 0 0 0 4.2 4.2L11 8.5l4 1.5v3a2 2 0 0 1-2 2A13 13 0 0 1 1 3a2 2 0 0 1 2-2z"/></svg>
          469.318.7742
        </li>
        <li>
          <svg viewBox="0 0 16 16" aria-label="Fax"><path d="M4 1h7l2 2v3H4z M1 7h14v6h-2v2H3v-2H1z M5 10v3h6v-3z"/></svg>
          469.318.7743
        </li>
        <li>
          <svg viewBox="0 0 16 16" aria-label="Email"><path d="M6.5 9.5l3-3M7 4l1.5-1.5a3 3 0 0 1 4 4L11 8M9 12l-1.5 1.5a3 3 0 0 1-4-4L5 8" stroke="#1e1e1e" stroke-width="1.8" fill="none" stroke-linecap="round"/></svg>
          info@vorlix.com
        </li>
        <li>
          <svg viewBox="0 0 16 16" aria-label="Address"><path d="M8 1l7 6.5h-2V15H9.5v-4h-3v4H3V7.5H1z"/></svg>
          2847 E. Hollowbrook Drive, STE 410 Marrowdale, TX 75981
        </li>
      </ul>
    </div>
  </section>

  <section class="card card-back" aria-label="Business card back">
    <div class="back-map" role="img" aria-label="Faint dotted world map decoration"></div>
    <div class="back-wordmark">vorlix</div>
  </section>

</main>
</body>
</html>
```